Quiet Lantern Revue Evening Postcard

Double sided post card. Front side a photo provided (Marta Quillon). Back, regular postcard design with logo provided as stamp (Quiet Lantern).

The University of Brackenmoor

```html
<!DOCTYPE html>
<html lang="en">
<head>
<meta charset="utf-8">
<title>Quiet Lantern Revue Evening Postcard</title>
<link rel="stylesheet" href="https://fonts.googleapis.com/css2?family=Open+Sans:wght@400;600;700&family=PT+Sans+Narrow:wght@400;700&display=swap">
<style>
  :root {
    --page: #ecebe8;
    --ink: #0c0a0b;
    --header-dark: #121012;
    --plum: #6e1e4f;
    --plum-deep: #3a0d2a;
    --plum-faint: #3b1a2c;
    --magenta: #ea1f8c;
    --gold: #d2a63c;
    --cream: #efe4c6;
    --cream-edge: #c9b27a;
    --ticket-ink: #4a1535;
    --line: #c8c8c8;
    --white: #ffffff;
    --stamp: #1f1d1f;
  }
  * { box-sizing: border-box; margin: 0; padding: 0; }
  html, body { width: 1200px; height: 1073px; overflow: hidden; }
  body { background: var(--page); position: relative; font-family: "Open Sans", sans-serif; }

  /* Back of postcard */
  .postcard-back {
    position: absolute; left: 63px; top: 40px; width: 728px; height: 566px;
    background: var(--white); overflow: hidden;
  }
  .back-header {
    position: absolute; left: 0; top: 0; width: 100%; height: 174px;
    background: linear-gradient(180deg, #000 0%, var(--header-dark) 100%);
    border-bottom-right-radius: 0 0;
  }
  .presenter-panel {
    position: absolute; left: 24px; top: 27px; width: 260px; height: 133px;
    background: linear-gradient(90deg, var(--plum-deep) 0%, #5a1a44 55%, #2a0b1f 100%);
  }
  .presenter-name {
    position: absolute; left: 50px; top: 36px;
    color: var(--magenta); font-weight: 700; font-size: 21px; letter-spacing: 0.2px;
    font-family: "PT Sans Narrow", sans-serif; text-transform: uppercase;
  }
  .presenter-verb {
    position: absolute; left: 70px; top: 74px;
    color: var(--white); font-size: 22px; letter-spacing: 6px;
  }
  .brand-mark {
    position: absolute; left: 292px; top: 60px; display: flex; align-items: center; gap: 10px;
  }
  .brand-mark .dot { width: 22px; height: 22px; border-radius: 50%; background: var(--magenta); }
  .brand-mark .name {
    color: var(--magenta); font-family: "PT Sans Narrow", sans-serif; font-weight: 700;
    font-size: 30px; text-transform: uppercase;
  }
  .stamp-box {
    position: absolute; left: 586px; top: 29px; width: 112px; height: 121px; background: var(--stamp);
  }
  .address-divider {
    position: absolute; left: 350px; top: 185px; width: 1px; height: 278px; background: var(--line);
  }
  .footer-rule {
    position: absolute; left: 0; top: 463px; width: 100%; height: 1px; background: var(--line);
  }

  .vip-invitation {
    position: absolute; left: 27px; top: 152px; width: 306px; height: 168px;
    transform: rotate(-3deg); box-shadow: 0 3px 6px rgba(0,0,0,0.35);
  }
  .vip-invitation .art {
    width: 100%; height: 100%;
    background: radial-gradient(circle at 45% 50%, #8a2a63 0%, var(--plum) 45%, #4d1238 100%);
  }
  .vip-invitation .seal {
    position: absolute; left: 92px; top: 24px; width: 120px; height: 120px; border-radius: 50%;
    border: 3px solid var(--gold); display: flex; flex-direction: column; align-items: center; justify-content: center;
    color: var(--gold); font-family: "PT Sans Narrow", sans-serif; font-weight: 700;
  }
  .seal .big { font-size: 34px; line-height: 1; margin-top: 18px; }
  .seal .small { font-size: 11px; letter-spacing: 1px; }
  .vip-invitation .tag {
    position: absolute; right: 12px; bottom: 12px; width: 38px; height: 24px; background: var(--magenta);
  }

  .vip-ticket {
    position: absolute; left: 27px; top: 307px; width: 301px; height: 148px;
    background: var(--cream); border: 3px solid var(--cream-edge);
    text-align: center; color: var(--ticket-ink); font-family: "PT Sans Narrow", sans-serif;
  }
  .vip-ticket .frame { position: absolute; inset: 6px; border: 1px solid var(--cream-edge); }
  .vip-ticket .title { margin-top: 18px; font-size: 27px; font-weight: 400; letter-spacing: 0.5px; }
  .vip-ticket .details { font-size: 14.5px; line-height: 1.3; }
  .vip-ticket .tag {
    position: absolute; right: 12px; bottom: 12px; width: 36px; height: 22px; background: var(--magenta);
  }

  /* Front of postcard */
  .postcard-front {
    position: absolute; left: 456px; top: 512px; width: 697px; height: 531px;
    background: var(--ink); overflow: hidden;
  }
  .front-photo {
    position: absolute; left: 40px; top: 0; width: 380px; height: 531px;
    background: linear-gradient(180deg, #1c1a1c 0%, #6b4a2a 18%, #2a2326 40%, #9c1d24 65%, #5e0f15 100%);
  }
  .front-decor { position: absolute; inset: 0; }
  .decor-word {
    font-family: "Open Sans", sans-serif; font-weight: 600; fill: #4a2438; text-transform: uppercase;
  }
</style>
</head>
<body>

<section class="postcard-back" aria-label="Postcard back">
  <header class="back-header">
    <div class="presenter-panel">
      <span class="presenter-name">Quiet Lantern</span>
      <span class="presenter-verb">PRESENTS</span>
    </div>
    <div class="brand-mark">
      <span class="dot"></span>
      <span class="name">Quiet Lantern</span>
    </div>
    <div class="stamp-box" aria-label="Stamp area"></div>
  </header>

  <div class="address-divider"></div>
  <div class="footer-rule"></div>

  <div class="vip-invitation">
    <div class="art" role="img" aria-label="Plum damask pattern background of the VIP invitation card"></div>
    <div class="seal">
      <span class="big">VIP</span>
      <span class="small">INVITATIONS</span>
    </div>
    <span class="tag"></span>
  </div>

  <div class="vip-ticket">
    <div class="frame"></div>
    <p class="title">VIP TICKET</p>
    <p class="details">for the Orchard Lamp Cabaret and Variety Showcase,<br>Friday 26 September 2014.<br>Entry from 7.30pm.</p>
    <span class="tag"></span>
  </div>
</section>

<section class="postcard-front" aria-label="Postcard front">
  <svg class="front-decor" width="697" height="531" viewBox="0 0 697 531" aria-hidden="true">
    <ellipse cx="560" cy="140" rx="175" ry="120" fill="#2b1422"/>
    <ellipse cx="560" cy="420" rx="175" ry="120" fill="#2b1422"/>
    <ellipse cx="20" cy="420" rx="90" ry="120" fill="#2b1422"/>
    <text class="decor-word" x="420" y="110" font-size="46">Quiet</text>
    <text class="decor-word" x="430" y="160" font-size="40">Lantern</text>
    <text class="decor-word" x="420" y="390" font-size="46">Quiet</text>
    <text class="decor-word" x="430" y="440" font-size="40">Lantern</text>
    <g stroke="#1f8f86" stroke-width="1" opacity="0.55" fill="none">
      <path d="M420 200 C 500 190, 600 215, 697 205"/>
      <path d="M420 210 C 510 200, 610 225, 697 220"/>
      <path d="M420 220 C 520 212, 620 238, 697 236"/>
    </g>
    <g fill="#ffffff">
      <circle cx="590" cy="112" r="6"/>
      <circle cx="520" cy="145" r="4"/>
      <circle cx="640" cy="255" r="5"/>
      <circle cx="570" cy="325" r="4"/>
      <circle cx="635" cy="288" r="15"/>
      <circle cx="525" cy="360" r="5"/>
      <circle cx="450" cy="390" r="4"/>
      <circle cx="600" cy="385" r="9"/>
      <circle cx="582" cy="420" r="5"/>
      <circle cx="45" cy="425" r="13"/>
      <circle cx="20" cy="320" r="4"/>
      <circle cx="440" cy="250" r="4"/>
    </g>
  </svg>
  <div class="front-photo" role="img" aria-label="Photograph of cabaret performer Marta Quillon in a red jewelled costume with a gold halo headdress"></div>
</section>

</body>
</html>
```